Brightwave Business Card

Professional Business Card Design required using the attached contact information.

Contact information can be rearranged as required.

The company is a new start up venture developing solar systems, the branding should be in keeping with that of one of the investors whose website is as follows https://www.quorvex.com/

```html
<!DOCTYPE html>
<html lang="en">
<head>
<meta charset="utf-8">
<title>Brightwave Energy – Business Card</title>
<link rel="stylesheet" href="https://fonts.googleapis.com/css2?family=Barlow:wght@600&family=Source+Sans+3:wght@400;600&display=swap">
<style>
  :root {
    --page-bg: #e9e9e9;
    --card-bg: #3b3b3d;
    --ink-light: #ffffff;
    --ink-dark: #2b2b2b;
    --shadow: rgba(0, 0, 0, 0.35);
  }
  * { box-sizing: border-box; margin: 0; padding: 0; }
  html, body {
    width: 1200px; height: 576px; overflow: hidden;
    background: var(--page-bg);
  }
  .sheet {
    position: relative; width: 1200px; height: 576px;
    display: flex; justify-content: center; align-items: center; gap: 40px;
  }
  .card {
    position: relative; width: 560px; height: 336px;
    background: var(--card-bg);
    box-shadow: 4px 6px 14px var(--shadow);
    overflow: hidden;
  }
  .brand-tab {
    position: absolute; left: 0; width: 298px; height: 52px;
    background: var(--ink-light);
    border-radius: 0 26px 26px 0;
    display: flex; align-items: center; padding-left: 25px;
  }
  .brand-name {
    font-family: "Source Sans 3", sans-serif; font-weight: 600;
    font-size: 20px; color: var(--ink-dark); white-space: nowrap;
  }
  .brand-rule {
    position: absolute; left: 290px; right: 0; height: 5px;
    background: var(--ink-light);
  }
  .card-front .brand-tab { top: 25px; }
  .card-front .brand-rule { top: 49px; }
  .card-back .brand-tab { top: 141px; }
  .card-back .brand-rule { top: 165px; }

  .holder-name {
    position: absolute; left: 17px; top: 94px;
    font-family: "Barlow", sans-serif; font-weight: 600;
    font-size: 37px; line-height: 1.1; color: var(--ink-light); letter-spacing: 0.3px;
  }
  .holder-underline {
    position: absolute; left: 17px; top: 142px; width: 70px; height: 3px;
    background: var(--ink-light);
  }
  .contact-list { list-style: none; }
  .contact-item {
    position: absolute; right: 24px;
    display: flex; align-items: center; gap: 10px;
    font-family: "Source Sans 3", sans-serif; font-size: 13.5px;
    color: var(--ink-light); text-align: right;
  }
  .contact-item svg { width: 21px; height: 21px; flex: none; }
  .contact-phone { top: 170px; }
  .contact-email { top: 208px; }
  .contact-web { top: 243px; }
  .contact-address { top: 281px; font-size: 12px; line-height: 1.3; text-align: left; }
</style>
</head>
<body>
<main class="sheet">
  <section class="card card-front" aria-label="Card front">
    <div class="brand-tab"><span class="brand-name">Brightwave Energy</span></div>
    <div class="brand-rule"></div>
    <h1 class="holder-name">Daniel Hollis</h1>
    <div class="holder-underline"></div>
    <ul class="contact-list">
      <li class="contact-item contact-phone">
        <span>+1 (555) 014-2738</span>
        <svg viewBox="0 0 24 24" aria-hidden="true"><circle cx="12" cy="12" r="11" fill="#fff"/><path d="M8.2 6.5c.5-.4 1.1-.3 1.4.2l1.2 2c.3.5.2 1-.2 1.4l-.8.7c.6 1.4 1.6 2.5 3 3.2l.7-.8c.4-.4.9-.5 1.4-.2l2 1.2c.5.3.6.9.2 1.4l-.9 1c-.6.6-1.6.8-2.5.4-3-1.3-5.4-3.7-6.6-6.7-.3-.9-.1-1.8.5-2.4z" fill="#3b3b3d"/></svg>
      </li>
      <li class="contact-item contact-email">
        <span>daniel.hollis@brightwave.com</span>
        <svg viewBox="0 0 24 24" aria-hidden="true"><rect x="2" y="5" width="20" height="14" fill="none" stroke="#fff" stroke-width="1.6"/><path d="M2 5l10 8 10-8M2 19l7.5-7M22 19l-7.5-7" fill="none" stroke="#fff" stroke-width="1.4"/></svg>
      </li>
      <li class="contact-item contact-web">
        <span>www.quorvex.com</span>
        <svg viewBox="0 0 24 24" aria-hidden="true"><g fill="none" stroke="#fff" stroke-width="1.3"><circle cx="12" cy="12" r="10"/><ellipse cx="12" cy="12" rx="4.5" ry="10"/><path d="M12 2v20M2 12h20M3.5 7h17M3.5 17h17"/></g></svg>
      </li>
      <li class="contact-item contact-address">
        <span>218 Harbor Street,<br>Easton, MA 02375</span>
        <svg viewBox="0 0 24 24" aria-hidden="true"><path d="M12 2a6.5 6.5 0 0 0-6.5 6.5c0 4.6 6.5 11 6.5 11s6.5-6.4 6.5-11A6.5 6.5 0 0 0 12 2z" fill="#fff"/><circle cx="12" cy="8.5" r="2.6" fill="#3b3b3d"/><ellipse cx="12" cy="21.5" rx="3.5" ry="1.1" fill="#fff"/></svg>
      </li>
    </ul>
  </section>

  <section class="card card-back" aria-label="Card back">
    <div class="brand-tab"><span class="brand-name">Brightwave Energy</span></div>
    <div class="brand-rule"></div>
  </section>
</main>
</body>
</html>
```